Design a Flyer for Maple and Crest Cleaning

NEW VECTORISED LOGO'S ATTACHED!

Need a 2 sided, postcard sized flyer.
On one side I would like the logo (attached), and the web address)

On the main side, I require the following information:

info@[login to view URL]
07841592067

-Book in 60 seconds, Online, Easy
-Teams on 2 for double the clean
-No contracts
-Simple flat-rate pricing
-Fully insured
-On-time service
-We also support charities

10% off with code 'leaflet13'.

Please use the colors from the 2 designs attached

```html
<!DOCTYPE html>
<html lang="en">
<head>
<meta charset="utf-8">
<title>Maple and Crest Cleaning – Postcard Flyer</title>
<link href="https://fonts.googleapis.com/css2?family=Open+Sans:wght@400;600;700&display=swap" rel="stylesheet">
<style>
  :root {
    --navy: #0d5aa7;
    --sky: #00aeef;
    --ink: #2b2b2b;
    --brand-blue: #3b72b9;
    --card-edge: #b9b9b9;
    --paper: #ffffff;
    --back-top: #1a8ad8;
    --back-bottom: #1061b4;
  }
  * { margin: 0; padding: 0; box-sizing: border-box; }
  html, body { width: 917px; height: 1200px; overflow: hidden; background: var(--paper); }
  body { position: relative; font-family: "Open Sans", Arial, sans-serif; color: var(--ink); }

  .card { position: absolute; left: 0; width: 917px; overflow: hidden; }

  /* Front side */
  .card--front {
    top: 0; height: 588px;
    border: 1px solid var(--card-edge);
    background: radial-gradient(circle at 330px 250px, #ffffff 0, #ffffff 90px, #f3f3f3 360px);
  }
  .front__pattern {
    position: absolute; left: 492px; top: 0; width: 425px; height: 588px;
    background: linear-gradient(135deg, var(--navy) 0%, var(--sky) 45%, var(--navy) 70%, var(--sky) 100%);
  }
  .brand-name {
    position: absolute; left: 58px; top: 92px;
    font-size: 27px; font-weight: 600; color: var(--brand-blue); letter-spacing: -0.3px;
  }
  .brand-name::before {
    content: ""; display: inline-block; width: 16px; height: 16px;
    background: var(--brand-blue); margin-right: 10px; vertical-align: 1px;
  }
  .features { position: absolute; left: 76px; top: 232px; list-style: none; }
  .features li {
    font-size: 15px; line-height: 25px; height: 25px; display: flex; align-items: center;
  }
  .features svg { width: 8px; height: 8px; margin-right: 12px; flex: none; }
  .offer-rule {
    position: absolute; left: 73px; top: 418px; width: 306px; height: 1px; background: var(--ink);
  }
  .offer {
    position: absolute; left: 73px; top: 420px; font-size: 18px; font-weight: 700;
  }
  .offer__code { color: var(--navy); }
  .contact-bar {
    position: absolute; left: 0; top: 511px; width: 66px; height: 34px; background: var(--navy);
  }
  .contact { position: absolute; left: 73px; top: 507px; font-size: 15px; line-height: 22px; }
  .contact__domain { font-weight: 700; }
  .contact__phone { font-weight: 700; font-size: 16px; }

  /* Back side */
  .card--back {
    top: 612px; height: 588px;
    background: linear-gradient(180deg, var(--back-top) 0%, #187ccd 50%, var(--back-bottom) 100%);
  }
  .back__brand {
    position: absolute; left: 0; right: 0; top: 218px; text-align: center;
    font-size: 38px; font-weight: 600; color: var(--paper); letter-spacing: -0.5px;
  }
  .back__web {
    position: absolute; left: 0; right: 0; top: 386px; text-align: center;
    font-size: 32px; color: var(--paper);
  }
  .back__web strong { font-weight: 600; }
</style>
</head>
<body>

<section class="card card--front">
  <div class="front__pattern" role="img" aria-label="Geometric pattern of dark blue, light blue and white triangles"></div>

  <div class="brand-name">Maple and Crest Cleaning</div>

  <ul class="features">
    <li><svg viewBox="0 0 8 8"><polygon points="8,0 8,8 0,8" fill="#0d5aa7"/></svg>Book in 60 seconds, Online, Easy</li>
    <li><svg viewBox="0 0 8 8"><polygon points="8,0 8,8 0,8" fill="#0d5aa7"/></svg>Teams on 2 for double the clean</li>
    <li><svg viewBox="0 0 8 8"><polygon points="8,0 8,8 0,8" fill="#0d5aa7"/></svg>No contracts</li>
    <li><svg viewBox="0 0 8 8"><polygon points="8,0 8,8 0,8" fill="#0d5aa7"/></svg>Simple flat-rate pricing</li>
    <li><svg viewBox="0 0 8 8"><polygon points="8,0 8,8 0,8" fill="#0d5aa7"/></svg>Fully insured</li>
    <li><svg viewBox="0 0 8 8"><polygon points="8,0 8,8 0,8" fill="#0d5aa7"/></svg>On-time service</li>
    <li><svg viewBox="0 0 8 8"><polygon points="8,0 8,8 0,8" fill="#0d5aa7"/></svg>We also support charities</li>
  </ul>

  <div class="offer-rule"></div>
  <p class="offer">10% off with code <span class="offer__code">'leaflet13'</span></p>

  <div class="contact-bar"></div>
  <div class="contact">
    <p>info@<span class="contact__domain">MapleandCrest</span>.com</p>
    <p class="contact__phone">07841592067</p>
  </div>
</section>

<section class="card card--back">
  <div class="back__brand">Maple and Crest Cleaning</div>
  <p class="back__web">www.<strong>MapleandCrest</strong>.com</p>
</section>

</body>
</html>
```